Brightpath Home & Upkeep Services, are a company that offers a 'one stop shop' pre-move clean up a

I have already selected a logo which I would like on the front of the business cards along with phone numbers, web address and email which are:
0419586402
www.brightpathhome.com.au
brightpathandupkeep@mailnest.com

On the back of the card I would like to list some of the types of service we offer (clean - move - repairs/maintenance) which are:
CLEAN - windows, gutters, solar panels, driveways/paths, carpets.
MOVE - Small/medium size house/office moves, large item pick-up & delivery, yard clean-up and removal.
General maintenance and repairs.

I would like the blue logo on a gray background.

Thanks

```html
<!DOCTYPE html>
<html lang="en">
<head>
<meta charset="utf-8">
<title>Brightpath Home &amp; Upkeep Services – Business Card</title>
<link rel="stylesheet" href="https://fonts.googleapis.com/css2?family=Arimo:wght@400;700&display=swap">
<style>
  :root {
    --brand-blue: #2470f5;
    --ink: #111111;
    --card-centre: #ffffff;
    --card-edge: #e4e4e4;
    --page: #ffffff;
  }
  * { margin: 0; padding: 0; box-sizing: border-box; }
  html, body {
    width: 1200px;
    height: 584px;
    overflow: hidden;
    background: var(--page);
    font-family: "Arimo", Arial, sans-serif;
    color: var(--ink);
  }
  .canvas {
    position: relative;
    width: 1200px;
    height: 584px;
  }
  .card {
    position: absolute;
    top: 115px;
    width: 483px;
    height: 287px;
    overflow: hidden;
    background: radial-gradient(ellipse 75% 72% at 50% 52%, var(--card-centre) 55%, var(--card-edge) 100%);
    text-align: center;
  }
  .card--front { left: 100px; }
  .card--back { left: 625px; }

  /* Front */
  .brand-name {
    position: absolute;
    left: 0; right: 0;
    top: 62px;
    display: flex;
    align-items: center;
    justify-content: center;
    gap: 10px;
    color: var(--brand-blue);
    font-weight: 700;
    font-size: 22px;
    line-height: 1.2;
  }
  .brand-name__mark {
    width: 22px;
    height: 22px;
    background: var(--brand-blue);
    border-radius: 3px;
    flex: none;
  }
  .contact {
    position: absolute;
    left: 0; right: 0;
    top: 178px;
    font-size: 14.5px;
    line-height: 19px;
    letter-spacing: 0.2px;
  }
  .website {
    position: absolute;
    left: 0; right: 0;
    top: 266px;
    font-size: 14.5px;
    letter-spacing: 0.2px;
  }

  /* Back */
  .services {
    position: absolute;
    left: 0; right: 0;
    top: 66px;
    font-size: 14px;
    line-height: 18px;
    letter-spacing: 0.2px;
  }
  .services__item { margin-bottom: 13px; }
  .services__item--general { margin-top: 20px; }
  .services__label {
    color: var(--brand-blue);
    font-weight: 700;
    font-size: 14.5px;
  }
  .service-band {
    position: absolute;
    left: 0; right: 0;
    bottom: 0;
    height: 24px;
    background: var(--brand-blue);
    border-radius: 7px 7px 0 0;
    color: #ffffff;
    font-size: 14.5px;
    line-height: 25px;
    letter-spacing: 0.3px;
  }
</style>
</head>
<body>
<main class="canvas">
  <section class="card card--front" aria-label="Business card front">
    <div class="brand-name">
      <span class="brand-name__mark" aria-hidden="true"></span>
      <span>Brightpath Home &amp; Upkeep Services</span>
    </div>
    <div class="contact">
      <p class="contact__phone">0419586402</p>
      <p class="contact__email">brightpathandupkeep@mailnest.com</p>
    </div>
    <p class="website">www.brightpathhome.com.au</p>
  </section>

  <section class="card card--back" aria-label="Business card back">
    <div class="services">
      <p class="services__item"><span class="services__label">CLEAN</span> - windows, gutters, solar panels,<br>driveways/paths, carpets.</p>
      <p class="services__item"><span class="services__label">MOVE</span> - Small/medium size house/office moves,<br>large item pick-up &amp; delivery, yard clean-up and removal.</p>
      <p class="services__item services__item--general">General <span class="services__label">Maintenance</span> and <span class="services__label">Repairs</span></p>
    </div>
    <div class="service-band">Clean • Move • Repairs / Maintenance</div>
  </section>
</main>
</body>
</html>
```